Community Management Cooperative Needs a Postcard Design

This will be the first postcard in a 3 part series to be sent to 2,500 management companies in the United States. Tellwood Residents Purchasing Alliance helps management companies and communities save money by combining their buying power to drive down costs on everyday business needs. Their membership in the cooperative also connects with other like minded companies in the industry allowing them to share ideas and best practices with one another so that they may improve their business practices. Visit http://jointrpa-hub.com for more information about the company.

The purpose of this postcard is to get potential members to visit our website to find out more about the cooperative and hopefully apply to become a member. This postcard should convey a message along the lines of "we want you" or "joining forces". I would like to use bright colors and make it eye catching. Can be things along the lines of (but not limited to) super heroes coming together or a patriotic theme, etc. Postcard does not have to be limited to company color palette but provided for reference.

Target Market(s)

Independent community management companies in the United States, mostly around metropolitan areas. CEO's of companies are usually male and older, 50+

Industry/Entity Type

Community

Requirements
Must have
• Must incorporate our name, logo, and website into the design with a call to action to visit the website.
• http://jointrpa-hub.com

```html
<!DOCTYPE html>
<html lang="en">
<head>
<meta charset="utf-8">
<title>Tellwood Residents Purchasing Alliance – Postcard</title>
<link href="https://fonts.googleapis.com/css2?family=Jost:wght@400;500;700&family=Open+Sans:wght@400;700&display=swap" rel="stylesheet">
<style>
  :root {
    --plum: #6e0f5c;
    --plum-deep: #5a0b4b;
    --lime: #cfe3a0;
    --lime-strong: #c6dd8d;
    --white: #ffffff;
    --ink-plum: #6b1a5a;
  }
  * { margin: 0; padding: 0; box-sizing: border-box; }
  html, body { width: 1200px; height: 772px; overflow: hidden; background: var(--white); }
  .postcard { position: relative; width: 1200px; height: 772px; overflow: hidden; font-family: "Open Sans", Arial, sans-serif; }

  .hero { position: absolute; left: 0; top: 0; width: 1200px; height: 598px;
    background: linear-gradient(90deg, var(--plum) 0%, var(--plum) 55%, var(--plum-deep) 100%); }

  .hero-photo { position: absolute; left: 450px; top: 0; width: 750px; height: 598px;
    background:
      linear-gradient(90deg, rgba(110,15,92,1) 0%, rgba(110,15,92,0) 14%),
      linear-gradient(90deg, #5d5a40 0%, #6a6748 18%, #2c3d7d 30%, #2c3d7d 52%, #b3283b 56%, #e0dcd8 64%, #b3283b 74%, #dcd8d4 84%, #6a6748 92%, #4a4734 100%); }

  .headline { position: absolute; left: 52px; top: 38px; font-family: "Jost", "Futura", sans-serif;
    font-weight: 700; font-size: 45px; line-height: 47px; letter-spacing: 1px; color: var(--lime); text-transform: uppercase; }
  .headline .accent { color: var(--white); }

  .intro { position: absolute; left: 52px; top: 246px; width: 370px; color: var(--white);
    font-size: 16.4px; line-height: 22px; }
  .intro strong { color: var(--lime-strong); font-weight: 700; }

  .promise { position: absolute; left: 52px; top: 518px; width: 360px; color: var(--lime-strong);
    font-weight: 700; font-size: 18px; line-height: 22px; }

  .rally { position: absolute; left: 560px; top: 500px; font-family: "Jost", "Futura", sans-serif;
    font-weight: 700; font-size: 74px; line-height: 80px; color: var(--white);
    text-shadow: 3px 4px 6px rgba(0,0,0,0.55); letter-spacing: 1px; white-space: nowrap; }

  .divider { position: absolute; left: 0; top: 598px; width: 1200px; height: 16px; background: var(--lime); }

  .brand { position: absolute; left: 82px; top: 640px; display: flex; align-items: center; gap: 18px; }
  .brand-square { width: 108px; height: 108px; background: var(--ink-plum); }
  .brand-name { font-family: "Jost", "Futura", sans-serif; font-weight: 500; color: var(--ink-plum);
    font-size: 25px; line-height: 33px; letter-spacing: 4px; text-transform: uppercase; }

  .cta { position: absolute; left: 630px; top: 645px; width: 490px; text-align: center; }
  .cta-line { font-family: "Jost", "Futura", sans-serif; font-size: 22px; color: var(--ink-plum);
    letter-spacing: 0.5px; text-transform: uppercase; }
  .cta-button { display: inline-block; margin-top: 16px; width: 346px; height: 50px; border: 3px solid var(--ink-plum);
    border-radius: 25px; background: var(--lime); font-family: "Jost", "Futura", sans-serif; font-size: 20px;
    line-height: 44px; color: var(--ink-plum); text-decoration: none; letter-spacing: 0.5px; }
  .cta-button b { font-weight: 700; }
</style>
</head>
<body>
<main class="postcard">
  <section class="hero">
    <div class="hero-photo" role="img" aria-label="Photo of a man pulling open his olive jacket to reveal an American flag shirt underneath"></div>

    <h1 class="headline">Demand a higher<br>standard of<br>performance.<br><span class="accent">We do</span></h1>

    <p class="intro"><strong>TRPA</strong> was created to bring the power of scale to companies and communities like yours. Our alliance works to enhance the value of all members through peer-to-peer networking, savings on products and services, and support for the entrepreneurial spirit. <strong>By joining forces</strong> with other likeminded members you are able to gain access to our PooledReach platform that leverages our memberships collective strength to offer programs and services independent companies and communities likely can’t achieve on their own.</p>

    <p class="promise">We help our members reduce the everyday costs of running a business.</p>

    <p class="rally">WE WANT YOU....</p>
  </section>

  <div class="divider"></div>

  <footer>
    <div class="brand">
      <div class="brand-square"></div>
      <div class="brand-name">Tellwood<br>Residents Purchasing<br>Alliance</div>
    </div>

    <div class="cta">
      <p class="cta-line">Join us now to get more information</p>
      <a class="cta-button" href="http://jointrpa-hub.com">WWW.<b>JOINTRPA-HUB</b>.COM</a>
    </div>
  </footer>
</main>
</body>
</html>
```